Business Card for Makeup Artist

I need a business card designed for my makeup and hair artistry business which is primarily events and weddings focused. The card needs to be sleek, simple, stylish and appealing to women. I would prefer a white background but open to suggestions also. I also love the marble background look. I have attached some example pics. It needs to be a double sided card with logo and/or design on one side and contact details in the centre of the card on the other side. NO LOGO ON BACK. Examples attached.

Target Market(s)

Females age 14-55

Industry/Entity Type

Business

Contact Information for Business Card

Nora Vint
Principal Makeup Artist
P: 0413 925 214
E: nora@lumirabeauty.com.au
W: www.lumirabeauty.com.au

Requirements
Should not have
• No yellow, green, red or blue in the design.

```html
<!DOCTYPE html>
<html lang="en">
<head>
<meta charset="utf-8">
<title>Lumira Makeup Artistry – Business Card</title>
<link rel="stylesheet" href="https://fonts.googleapis.com/css2?family=Questrial&display=swap">
<style>
  :root {
    --backdrop: #2e2c2b;
    --marble-light: #f7f7f7;
    --marble-mid: #e6e6e7;
    --marble-vein: #cfd0d2;
    --gold-dark: #b39a6c;
    --gold-light: #d8c49a;
    --charcoal: #4c4847;
    --ink-light: #ffffff;
    --logo-grey: #6f6e6e;
  }
  html, body {
    margin: 0;
    padding: 0;
    width: 1200px;
    height: 1200px;
    overflow: hidden;
    background: var(--backdrop);
    font-family: "Questrial", sans-serif;
  }
  .canvas {
    position: relative;
    width: 1200px;
    height: 1200px;
  }
  .card {
    position: absolute;
    left: 250px;
    width: 700px;
    height: 400px;
    overflow: hidden;
    box-shadow: 0 14px 30px rgba(0,0,0,0.45);
  }
  .card--front { top: 150px; }
  .card--back  { top: 650px; }

  .marble {
    position: absolute;
    inset: 0;
    background:
      radial-gradient(ellipse at 25% 30%, var(--marble-mid) 0%, transparent 45%),
      radial-gradient(ellipse at 75% 70%, var(--marble-vein) 0%, transparent 40%),
      linear-gradient(135deg, var(--marble-light) 0%, var(--marble-mid) 50%, var(--marble-light) 100%);
  }

  .gold-band {
    position: absolute;
    left: 0;
    right: 0;
    top: 150px;
    height: 56px;
    background: linear-gradient(90deg, var(--gold-light) 0%, var(--gold-dark) 35%, var(--gold-light) 70%, var(--gold-dark) 100%);
  }

  .contact-panel {
    position: absolute;
    left: 210px;
    top: 95px;
    width: 280px;
    height: 255px;
    background: var(--charcoal);
    color: var(--ink-light);
    box-sizing: border-box;
    padding: 26px 22px 20px 26px;
  }
  .contact-panel__name {
    margin: 0;
    font-size: 44px;
    font-weight: 400;
    line-height: 1;
    letter-spacing: 0.5px;
  }
  .contact-panel__title {
    margin: 12px 0 0;
    font-size: 14px;
    letter-spacing: 1.6px;
    text-transform: uppercase;
  }
  .contact-panel__details {
    margin: 26px 0 0;
    padding: 0;
    list-style: none;
    text-align: right;
    font-size: 15px;
    line-height: 1.45;
  }
  .contact-panel__details li:first-child { margin-bottom: 10px; }

  .brand-frame {
    position: absolute;
    left: 175px;
    top: 95px;
    width: 350px;
    height: 200px;
    box-sizing: border-box;
    border: 4px solid var(--gold-dark);
    display: flex;
    flex-direction: column;
    align-items: center;
    justify-content: center;
    color: var(--logo-grey);
  }
  .brand-frame__name {
    font-size: 56px;
    letter-spacing: 6px;
    line-height: 1;
  }
  .brand-frame__tagline {
    margin-top: 10px;
    font-size: 18px;
    letter-spacing: 2px;
  }
</style>
</head>
<body>
<main class="canvas">
  <section class="card card--front" aria-label="Business card contact side">
    <div class="marble" role="img" aria-label="White marble texture with soft grey veining"></div>
    <div class="gold-band"></div>
    <div class="contact-panel">
      <h1 class="contact-panel__name">Nora Vint</h1>
      <p class="contact-panel__title">Principal Makeup Artist</p>
      <ul class="contact-panel__details">
        <li>0413 925 214</li>
        <li>nora@lumirabeauty.com.au</li>
        <li>www.lumirabeauty.com.au</li>
      </ul>
    </div>
  </section>

  <section class="card card--back" aria-label="Business card brand side">
    <div class="marble" role="img" aria-label="White marble texture with soft grey veining"></div>
    <div class="brand-frame">
      <span class="brand-frame__name">LUMIRA</span>
      <span class="brand-frame__tagline">MAKEUP ARTISTRY</span>
    </div>
  </section>
</main>
</body>
</html>
```